Vro Klinieken website for a maxillofacial surgery clinic

It's a website for a clinic for maxillofacial surgery in WordPress . The website doesn't need to be complicated but has to look professional. It needs to be in Dutch so i can give the texts. Similar websites are www.tandartsenpraktijkvelmor.nl or www.tbospecialisten.nl. Pages would be sort of similar to https://hetcentrumvoorgezichtszorg.nl/ or https://wolderveenclinics.nl/. Those lasts are maxillofacial surgery clinic websites, but there are little more extensive.
I uploaded the logo. If this is not the proper quality i can upload the eps. Logo was made through printhive.

Target Market(s)

Patients who can find me and see information about the clinic

Industry/Entity Type

Healthcare

Coding

Coded - Design and coding required

Number of Pages Required

5+ page

Font styles to use
Other font styles liked:
• Something standard professional

Colors
0054AA
0677BA
7BADD7
CADEEF
E8F1F8

Requirements
Nice to have
• Something in line with the logo. I prefer a little dark like the darker logos but I'm not sure if that's professional. Logos zbpor and gvls are instances i'm registered to so they will have to be on the website too but small somewhere.

```html
<!DOCTYPE html>
<html lang="nl">
<head>
<meta charset="utf-8">
<title>Vro Klinieken – websiteontwerp</title>
<link href="https://fonts.googleapis.com/css2?family=Open+Sans:wght@400;600;700;800&display=swap" rel="stylesheet">
<style>
:root{
  --blue:#2b9ad8;
  --blue-deep:#0677ba;
  --nav:#6b7fa0;
  --nav-active:#2b9ad8;
  --navy:#323d52;
  --ink:#1d2330;
  --text:#3a3f4a;
  --light:#d8ecf8;
  --slate:#6e84a6;
  --white:#ffffff;
  --photo-a:#e9d7cc;
}
*{box-sizing:border-box;margin:0;padding:0}
html,body{width:1200px;height:1200px;overflow:hidden;background:var(--white)}
body{font-family:"Open Sans",Arial,sans-serif;color:var(--text)}
.board{position:absolute;left:0;top:0;width:1932px;height:1932px;transform:scale(.6211);transform-origin:0 0}
.page{position:absolute;width:475px;background:var(--white);box-shadow:0 0 4px rgba(0,0,0,.12);display:flex;flex-direction:column;overflow:hidden}

.site-header{height:52px;display:flex;align-items:center;padding:0 0 0 68px;position:relative}
.brand{font-weight:700;font-size:13px;color:var(--blue-deep);width:122px;letter-spacing:.2px}
.contact-chip{display:flex;align-items:center;gap:4px;font-size:5.5px;line-height:1.3;color:var(--ink);font-weight:600;margin-right:8px}
.chip-dot{width:12px;height:12px;border-radius:50%;background:var(--blue)}
.btn{background:var(--blue);color:var(--white);font-size:5.5px;font-weight:700;padding:5px;text-transform:uppercase;white-space:nowrap}
.site-nav{height:20px;background:var(--nav);display:flex;align-items:center;padding-left:70px}
.site-nav a{color:var(--white);font-size:5.3px;text-transform:uppercase;text-decoration:none;padding:7px 3.5px;line-height:6px}
.site-nav a.active{background:var(--nav-active)}

.hero{position:relative;height:140px;background:#f5f7fa;overflow:hidden}
.hero .photo{position:absolute;right:0;top:0;width:62%;height:100%;background:linear-gradient(100deg,#eef1f5 0%,var(--photo-a) 45%,#d8c2b4 100%)}
.hero h1{position:absolute;left:68px;top:22px;font-weight:800;font-size:22px;line-height:1;color:var(--ink);text-transform:uppercase;z-index:2}
.hero h1.small{font-size:13px;line-height:1.2}
.hero .sub{position:absolute;left:68px;top:50px;font-size:13px;color:var(--ink);z-index:2}
.hero .wave{position:absolute;left:0;bottom:0;width:100%;height:40px;z-index:3}
.hero-home{height:260px;background:linear-gradient(90deg,#fafafa 0%,#f3eee9 45%,var(--photo-a) 70%,#caa792 100%)}
.hero-home .photo{width:50%;background:linear-gradient(90deg,#f3eee9 0%,#d9b8a4 60%,#c8a08a 100%)}

.section-title{text-align:center;font-weight:800;font-size:12px;color:var(--ink);text-transform:uppercase;margin-top:24px}
.body-text{font-size:4.6px;line-height:1.75;text-align:center;color:var(--text);padding:0 66px}

.site-footer{margin-top:auto;position:relative;background:var(--navy);color:var(--white)}
.site-footer .wave{display:block;width:100%;height:42px;background:var(--white)}
.footer-body{position:relative;height:158px}
.footer-brand{position:absolute;left:70px;top:40px;font-size:24px;font-weight:700;color:var(--white);width:130px;line-height:1.05}
.footer-col{position:absolute;top:14px}
.footer-col h4{font-size:8.5px;font-weight:700;text-transform:uppercase;margin-bottom:6px}
.footer-col ul{list-style:none;font-size:4.8px;line-height:1.8;text-transform:uppercase}
.links{left:217px}
.details{left:305px}
.detail{display:flex;gap:5px;font-size:5.2px;line-height:1.4;margin-bottom:9px}
.detail .ic{width:11px;height:11px;border-radius:50%;background:var(--blue);flex:none}
.footer-rule{position:absolute;left:68px;right:68px;top:124px;border-top:1px solid #5b6579}
.copy{position:absolute;left:0;right:0;top:136px;text-align:center;font-size:5.3px}

.intro{height:138px;position:relative}
.intro h2{position:absolute;left:120px;top:30px;font-size:11px;font-weight:600;color:var(--ink);line-height:1.1;width:300px}
.intro p{position:absolute;left:175px;top:62px;width:236px;font-size:4.7px;line-height:1.7;text-align:justify}
.clinic{height:262px;background:var(--slate);position:relative}
.clinic h2{position:absolute;left:0;right:0;top:26px;text-align:center;color:var(--white);font-size:12px;font-weight:700}
.cards3{position:absolute;left:68px;top:98px;display:flex;gap:6px}
.card3{width:108px;height:155px;background:var(--white);text-align:center;position:relative;padding:36px 5px 0;box-shadow:0 1px 3px rgba(0,0,0,.2)}
.card3 .ico{position:absolute;left:31px;top:-24px;width:46px;height:46px;border-radius:50%;background:var(--slate);border:3px solid var(--white);box-shadow:0 0 0 1px #c0c8d6}
.card3 h3{font-size:7.3px;font-weight:800;color:var(--ink);line-height:1.1;margin-bottom:4px}
.card3 p{font-size:4.4px;line-height:1.55}
.treat{height:240px;position:relative}
.treat .photo{position:absolute;right:0;top:-50px;width:175px;height:290px;background:linear-gradient(160deg,#f4ece6 0%,var(--photo-a) 50%,#cfae9b 100%)}
.treat h2{position:absolute;left:80px;top:20px;font-size:11px;font-weight:800;color:var(--ink)}
.treat .lead{position:absolute;left:103px;top:36px;font-size:4.7px;width:130px;line-height:1.5}
.treat ul{position:absolute;left:70px;top:58px;list-style:none}
.treat li{display:flex;align-items:center;gap:6px;font-size:5.6px;font-weight:600;color:var(--ink);height:21px;width:200px;line-height:1.2}
.treat li i{width:13px;height:13px;border-radius:50%;background:var(--slate);flex:none}
.testi{height:230px;background:var(--light);position:relative}
.testi .ph{position:absolute;border:2px solid var(--white);background:linear-gradient(135deg,#c9d6e4,#8ea6bf)}
.stars{position:absolute;left:262px;top:40px;font-size:13px;color:#8b8f98;letter-spacing:1px}
.stars b{color:#bfc3ca;font-weight:400}
.testi h3{position:absolute;left:262px;top:70px;font-size:8px;font-weight:800;color:var(--ink)}
.testi p{position:absolute;left:262px;top:86px;width:148px;font-size:4.6px;line-height:1.7}
.testi .who{position:absolute;left:262px;top:142px;font-size:5px}
.arrows{position:absolute;left:264px;top:164px;font-size:14px;color:var(--ink)}

.framed{margin:16px auto 0;width:337px;height:205px;border:3px solid var(--white);box-shadow:0 1px 4px rgba(0,0,0,.3);position:relative;background:linear-gradient(120deg,#9fb7cf 0%,#dfe6ee 45%,#c6ccd3 100%)}
.framed .label{position:absolute;right:0;bottom:6px;background:var(--blue);color:var(--white);font-size:8px;font-weight:600;padding:4px 8px}

.afs-lead{font-size:4.8px;line-height:1.7;text-align:center;padding:0 60px;margin-top:14px}
.afs-row{display:flex;gap:10px;padding:0 66px;margin-top:14px}
.afs-row ul{font-size:4.8px;line-height:1;padding-left:8px;margin-top:26px;width:190px}
.afs-row li{margin-bottom:7px}
.map{width:142px;height:115px;background:linear-gradient(135deg,#efe9df,#e8d9cc 50%,#dde3ea);box-shadow:0 1px 3px rgba(0,0,0,.3);border:3px solid var(--white)}

.vcards{margin:18px auto 0;width:340px}
.vcard{height:93px;background:var(--white);box-shadow:0 0 3px rgba(0,0,0,.25);margin-bottom:7px;display:flex;padding:3px;gap:6px}
.vcard.tall{height:118px}
.vcard .img{width:95px;flex:none;background:linear-gradient(135deg,#bccbdb,#6f87a3)}
.vcard h3{font-size:7px;font-weight:700;color:var(--ink);margin:10px 0 4px}
.vcard p{font-size:4.3px;line-height:1.6;text-align:justify;padding-right:4px}

.kgrid{display:grid;grid-template-columns:162px 162px;gap:10px 12px;justify-content:center;margin-top:14px}
.kcard{height:153px;box-shadow:0 0 3px rgba(0,0,0,.25);background:var(--white);padding:3px;text-align:center}
.kcard .img{height:97px;background:linear-gradient(135deg,#d6e2ec,#9ab2c8)}
.kcard h3{font-size:6.3px;font-weight:700;color:var(--ink);margin:8px 0 3px}
.kcard p{font-size:4.2px;line-height:1.55;padding:0 4px}
</style>
</head>
<body>
<div class="board">

<section class="page" style="left:5px;top:128px;height:1402px">
  <header class="site-header">
    <div class="brand">Vro Klinieken</div>
    <div class="contact-chip"><span class="chip-dot"></span><span>Mail:<br>info@vroklinieken.nl</span></div>
    <div class="contact-chip"><span class="chip-dot"></span><span>Phone Number<br>079 204 5518</span></div>
    <div class="btn">Make an appointment</div>
  </header>
  <nav class="site-nav"><a class="active">Home</a><a>Over ons</a><a>Vergoeding</a><a>Klachtbehandeling</a><a>Duurzaamheid / Duurzame mondzorg</a><a>Contact</a></nav>
  <div class="hero hero-home">
    <div class="photo" role="img" aria-label="Portret van een lachende vrouw met stralend gebit"></div>
    <h1 style="top:42px;font-size:24px">Vro Klinieken</h1>
    <div class="sub" style="top:74px;font-size:14px">ZOETERMEER</div>
    <div class="btn" style="position:absolute;left:68px;top:104px;z-index:2">Call for an appointment</div>
    <div style="position:absolute;left:69px;top:140px;display:flex;gap:3px;z-index:2"><i style="width:4px;height:4px;border-radius:50%;background:#2d3a55"></i><i style="width:4px;height:4px;border-radius:50%;background:#b7bfcc"></i><i style="width:4px;height:4px;border-radius:50%;background:#b7bfcc"></i></div>
    <svg class="wave" viewBox="0 0 475 40" preserveAspectRatio="none"><path d="M0 40 L0 28 C140 -4 330 12 475 4 L475 40Z" fill="#2b9ad8"/><path d="M0 40 L0 36 C150 8 330 22 475 14 L475 40Z" fill="#fff"/></svg>
  </div>
  <div class="intro">
    <h2>VRO KLINIEKEN OFFERS SOLUTIONS FOR ALL YOUR DENTAL PROBLEMS</h2>
    <p>Welkom bij Vro Klinieken, een nieuwe kliniek in Zoetermeer voor Mondziekten Kaak- en Aangezichtschirurgie. Ons ervaren team staat klaar om u de hoogste kwaliteit van zorg te bieden en een persoonlijke benadering.</p>
  </div>
  <div class="clinic">
    <h2>THE CLINIC</h2>
    <div class="cards3">
      <div class="card3"><div class="ico"></div><h3>ONZE DIENSTEN</h3><p>Ontdek een breed scala aan diensten, variërend van routine-ingrepen tot complexe behandelingen. Onze kliniek richt zich op het verwijderen van gebitselementen, implantologie, kaakchirurgie en slaapapneu, met als doel uw welzijn te verbeteren.</p></div>
      <div class="card3"><div class="ico"></div><h3>PROFESSIONEEL TEAM</h3><p>Ons deskundig team is gepassioneerd om uw vertrouwen te verdienen. Wij luisteren naar uw behoeften, beantwoorden uw vragen en zorgen voor een geruststellende ervaring tijdens uw bezoek.</p></div>
      <div class="card3"><div class="ico"></div><h3>PATIËNTENZORG STAAT VOOROP</h3><p>Uw comfort en tevredenheid zijn onze topprioriteit. Wij streven naar open communicatie en transparantie, zodat u zich volledig geïnformeerd voelt. Neem vandaag nog contact met ons op voor een afspraak via 000-000000.</p></div>
    </div>
  </div>
  <div class="treat">
    <div class="photo" role="img" aria-label="Profielfoto van een vrouw met verzorgde kaaklijn"></div>
    <h2>BEHANDELINGEN</h2>
    <div class="lead">Hieronder kunt u onze informatiefolders over de behandelingen bekijken.</div>
    <ul>
      <li><i></i>Verwijderen van (verstands)kiezen of gebitselementen</li>
      <li><i></i>De apexresectie of wortelpuntbehandeling</li>
      <li><i></i>Het vrijleggen van niet doorbrekende gebitselementen</li>
      <li><i></i>Vervanging gebitselementen door tandheelkundige implantaten (orale implantologie)</li>
      <li><i></i>Verbinding naar neusbijholte</li>
      <li><i></i>Kaakcorrecties</li>
      <li><i></i>Kaakgewrichtsklachten</li>
      <li><i></i>Mond- en tongbranden</li>
    </ul>
  </div>
  <div class="testi">
    <div class="ph" role="img" aria-label="Foto van een tandheelkundige behandeling" style="left:68px;top:22px;width:78px;height:62px"></div>
    <div class="ph" role="img" aria-label="Foto van een patiënte in de behandelstoel" style="left:120px;top:58px;width:126px;height:68px"></div>
    <div class="ph" role="img" aria-label="Foto van een chirurgisch team aan het werk" style="left:45px;top:88px;width:72px;height:70px"></div>
    <div class="ph" role="img" aria-label="Foto van een gezichtsbehandeling" style="left:116px;top:128px;width:106px;height:68px"></div>
    <div class="stars">★★★<b>★★</b></div>
    <h3>CLIENT TESTIMONIALS</h3>
    <p>Nemo enim ipsam voluptatem quia voluptas sit aspernatur aut odit aut fugit, sed quia consequuntur magni dolores eos qui ratione voluptatem sequi nesciunt. Neque porro quisquam est, qui dolorem ipsum quia dolor sit amet, consectetur, adipisci velit, sed quia non numquam eius modi tempora incidunt ut labore et dolore magnam aliquam quaerat voluptatem.</p>
    <div class="who">- John Smith</div>
    <div class="arrows">‹ ›</div>
  </div>
  <footer class="site-footer">
    <svg class="wave" viewBox="0 0 475 42" preserveAspectRatio="none"><path d="M0 42 L0 14 C130 44 300 40 475 0 L475 42Z" fill="#2b9ad8"/><path d="M0 42 L0 24 C130 50 310 42 475 14 L475 42Z" fill="#323d52"/></svg>
    <div class="footer-body">
      <div class="footer-brand">Vro Klinieken</div>
      <div class="footer-col links"><h4>Quick links</h4><ul><li>Home</li><li>Over ons</li><li>Vergoeding</li><li>Klachtbehandeling</li><li>Duurzaamheid</li><li>Duurzame mondzorg</li><li>Contact</li></ul></div>
      <div class="footer-col details"><h4>Contact details</h4>
        <div class="detail"><i class="ic"></i><span>Lindenhof 14<br>2711 AB Zoetermeer</span></div>
        <div class="detail"><i class="ic"></i><span>Phone Number<br>079 204 5518</span></div>
        <div class="detail"><i class="ic"></i><span>Mail ID:<br>info@vroklinieken.nl</span></div>
      </div>
      <div class="footer-rule"></div>
      <div class="copy">Copyrights @ 2023 Vro Klinieken. All Rights Reserved.</div>
    </div>
  </footer>
</section>

<section class="page" style="left:490px;top:128px;height:832px">
  <header class="site-header">
    <div class="brand">Vro Klinieken</div>
    <div class="contact-chip"><span class="chip-dot"></span><span>Mail:<br>info@vroklinieken.nl</span></div>
    <div class="contact-chip"><span class="chip-dot"></span><span>Phone Number<br>079 204 5518</span></div>
    <div class="btn">Make an appointment</div>
  </header>
  <nav class="site-nav"><a>Home</a><a class="active">Over ons</a><a>Vergoeding</a><a>Klachtbehandeling</a><a>Duurzaamheid / Duurzame mondzorg</a><a>Contact</a></nav>
  <div class="hero">
    <div class="photo" role="img" aria-label="Patiënte in de behandelstoel met tandarts"></div>
    <h1 style="top:26px">Over ons</h1>
    <div class="sub" style="top:52px">DRS. L. MARSEN</div>
    <svg class="wave" viewBox="0 0 475 40" preserveAspectRatio="none"><path d="M0 40 L0 20 C140 -4 330 12 475 4 L475 40Z" fill="#2b9ad8"/><path d="M0 40 L0 28 C150 6 330 26 475 14 L475 40Z" fill="#6b7fa0"/><path d="M0 40 L0 34 C150 14 330 32 475 20 L475 40Z" fill="#fff"/></svg>
  </div>
  <h2 class="section-title">Over ons</h2>
  <div class="framed" role="img" aria-label="Portretfoto van de kaakchirurg in witte jas"><div class="label">DRS. L. MARSEN</div></div>
  <p class="body-text" style="margin-top:22px">L. Marsen heeft zijn studie tandheelkunde in 2009 afgerond. Achtereenvolgens begon hij met geneeskunde en in 2014 startte hij aan de opleiding Mondziekten Kaak- en Aangezichtschirurgie aan een academisch ziekenhuis, die hij in 2018 heeft afgerond. Sindsdien heeft hij op meerdere locaties waargenomen en sinds 2020 is hij parttime werkzaam als kaakchirurg. Hij is gespecialiseerd in botzetten, orthognathische chirurgie en speekselklierpathologie. Daarnaast doet hij onderzoek naar kunstmatige intelligentie in de mondzorg en naar osteomyelitis en botzetten. Tevens gaat zijn interesse uit naar tandheelkundige slaapapneu, implantologie en gecombineerde chirurgische orthodontische behandelingen.<br>In 2017 behaalde hij de accreditatie voor tandheelkundige slaapgeneeskunde en voor de aangezichtschirurgie. In 2021 heeft hij samen met een collega parodontoloog een kliniek opgericht, gespecialiseerd op de vervaardiging van apparaten voor slaapapneu (www.tbospecialisten.nl).<br>L. Marsen neemt verder nog zitting in verschillende commissies binnen de beroepsvereniging voor kaakchirurgen (ZBPOR).</p>
  <footer class="site-footer">
    <svg class="wave" viewBox="0 0 475 42" preserveAspectRatio="none"><path d="M0 42 L0 14 C130 44 300 40 475 0 L475 42Z" fill="#2b9ad8"/><path d="M0 42 L0 24 C130 50 310 42 475 14 L475 42Z" fill="#323d52"/></svg>
    <div class="footer-body">
      <div class="footer-brand">Vro Klinieken</div>
      <div class="footer-col links"><h4>Quick links</h4><ul><li>Home</li><li>Over ons</li><li>Vergoeding</li><li>Klachtbehandeling</li><li>Duurzaamheid</li><li>Duurzame mondzorg</li><li>Contact</li></ul></div>
      <div class="footer-col details"><h4>Contact details</h4>
        <div class="detail"><i class="ic"></i><span>Lindenhof 14<br>2711 AB Zoetermeer</span></div>
        <div class="detail"><i class="ic"></i><span>Phone Number<br>079 204 5518</span></div>
        <div class="detail"><i class="ic"></i><span>Mail ID:<br>info@vroklinieken.nl</span></div>
      </div>
      <div class="footer-rule"></div>
      <div class="copy">Copyrights @ 2023 Vro Klinieken. All Rights Reserved.</div>
    </div>
  </footer>
</section>

<section class="page" style="left:970px;top:128px;height:667px">
  <header class="site-header">
    <div class="brand">Vro Klinieken</div>
    <div class="contact-chip"><span class="chip-dot"></span><span>Mail:<br>info@vroklinieken.nl</span></div>
    <div class="contact-chip"><span class="chip-dot"></span><span>Phone Number<br>079 204 5518</span></div>
    <div class="btn">Make an appointment</div>
  </header>
  <nav class="site-nav"><a>Home</a><a>Over ons</a><a>Vergoeding</a><a>Klachtbehandeling</a><a>Duurzaamheid / Duurzame mondzorg</a><a class="active">Contact</a></nav>
  <div class="hero">
    <div class="photo" role="img" aria-label="Patiënte in de behandelstoel met tandarts"></div>
    <h1 class="small" style="top:34px">Afspraak en<br>contact</h1>
    <svg class="wave" viewBox="0 0 475 40" preserveAspectRatio="none"><path d="M0 40 L0 20 C140 -4 330 12 475 4 L475 40Z" fill="#2b9ad8"/><path d="M0 40 L0 28 C150 6 330 26 475 14 L475 40Z" fill="#6b7fa0"/><path d="M0 40 L0 34 C150 14 330 32 475 20 L475 40Z" fill="#fff"/></svg>
  </div>
  <h2 class="section-title">Afspraak en contact</h2>
  <p class="afs-lead">Voor het maken van een afspraak kunt u telefonisch contact opnemen op het telefoonnummer 000-000000 of kunt u een mail sturen naar info@vroklinieken.nl.<br><br>Voor uw eerste afspraak vragen wij u het volgende mee te nemen of vooraf te mailen naar info@vroklinieken.nl.</p>
  <div class="afs-row">
    <ul>
      <li>Uw verwijzing van tandarts/huisarts/verwijzend specialist</li>
      <li>Een Actueel Medicatie Overzicht (verkrijgbaar bij uw apotheek)</li>
      <li>Identiteitsbewijs</li>
      <li>Verzekeringsbewijs (polisnummer)</li>
      <li>Eventuele röntgenfoto's van uw tandarts/verwijzer</li>
    </ul>
    <div class="map" role="img" aria-label="Kaart met de locatie van de kliniek"></div>
  </div>
  <footer class="site-footer">
    <svg class="wave" viewBox="0 0 475 42" preserveAspectRatio="none"><path d="M0 42 L0 14 C130 44 300 40 475 0 L475 42Z" fill="#2b9ad8"/><path d="M0 42 L0 24 C130 50 310 42 475 14 L475 42Z" fill="#323d52"/></svg>
    <div class="footer-body">
      <div class="footer-brand">Vro Klinieken</div>
      <div class="footer-col links"><h4>Quick links</h4><ul><li>Home</li><li>Over ons</li><li>Vergoeding</li><li>Klachtbehandeling</li><li>Duurzaamheid</li><li>Duurzame mondzorg</li><li>Contact</li></ul></div>
      <div class="footer-col details"><h4>Contact details</h4>
        <div class="detail"><i class="ic"></i><span>Lindenhof 14<br>2711 AB Zoetermeer</span></div>
        <div class="detail"><i class="ic"></i><span>Phone Number<br>079 204 5518</span></div>
        <div class="detail"><i class="ic"></i><span>Mail ID:<br>info@vroklinieken.nl</span></div>
      </div>
      <div class="footer-rule"></div>
      <div class="copy">Copyrights @ 2023 Vro Klinieken. All Rights Reserved.</div>
    </div>
  </footer>
</section>

<section class="page" style="left:1450px;top:128px;height:1134px">
  <header class="site-header">
    <div class="brand">Vro Klinieken</div>
    <div class="contact-chip"><span class="chip-dot"></span><span>Mail:<br>info@vroklinieken.nl</span></div>
    <div class="contact-chip"><span class="chip-dot"></span><span>Phone Number<br>079 204 5518</span></div>
    <div class="btn">Make an appointment</div>
  </header>
  <nav class="site-nav"><a>Home</a><a>Over ons</a><a class="active">Vergoeding</a><a>Klachtbehandeling</a><a>Duurzaamheid / Duurzame mondzorg</a><a>Contact</a></nav>
  <div class="hero">
    <div class="photo" role="img" aria-label="Patiënte in de behandelstoel met tandarts"></div>
    <h1 style="top:34px">Vergoeding</h1>
    <svg class="wave" viewBox="0 0 475 40" preserveAspectRatio="none"><path d="M0 40 L0 20 C140 -4 330 12 475 4 L475 40Z" fill="#2b9ad8"/><path d="M0 40 L0 28 C150 6 330 26 475 14 L475 40Z" fill="#6b7fa0"/><path d="M0 40 L0 34 C150 14 330 32 475 20 L475 40Z" fill="#fff"/></svg>
  </div>
  <h2 class="section-title">Vergoeding</h2>
  <div class="vcards">
    <div class="vcard"><div class="img" role="img" aria-label="Rekenmachine en papieren op een bureau"></div><div><h3>Kosten en Vergoedingen</h3><p>Bij Vro Klinieken begrijpen we dat helderheid over kosten en vergoedingen essentieel is voor onze patiënten. Hier vindt u informatie over onze tarieven en de mogelijkheden voor vergoedingen.</p></div></div>
    <div class="vcard tall"><div class="img" role="img" aria-label="Handdruk aan een bureau bij een adviesgesprek"></div><div><h3>Verzekerde zorg</h3><p>Voor vergoeding van behandelingen in onze kliniek is een verwijzing van uw tandarts, huisarts of een andere verwijzende specialist vereist. Behandelingen worden veelal vergoed vanuit de basisverzekering. Het is belangrijk om rekening te houden met uw verplichte eigen risico. Wij hebben nog geen contracten afgesloten met zorgverzekeraars, waardoor een deel zelf betaald kan worden. Om onze patiënten geen extra drempel op te leggen, hebben we ervoor gekozen dat u geen eigen bijdrage hoeft te betalen. Let op: de eigen bijdrage is niet hetzelfde als het eigen risico.</p></div></div>
    <div class="vcard"><div class="img" role="img" aria-label="Zorgverlener aan het werk achter een laptop"></div><div><h3>Facturering</h3><p>Het declaratieproces voor zorgkosten wordt verzorgd door een extern factuurbedrijf. U ontvangt de factuur voor de behandeling via dit bedrijf. Het door uw verzekering vergoede deel dient u zelf te betalen.<br><br>Houd er rekening mee dat uw behandeling niet volledig wordt vergoed door uw verzekeringsmaatschappij.</p></div></div>
    <div class="vcard"><div class="img" role="img" aria-label="Handen beschermen een papieren gezin"></div><div><h3>Onverzekerde zorg</h3><p>Hieronder valt zorg die door de kliniek kan worden geleverd die niet onder de basisverzekering valt, zoals de plaatsing van implantaten. U zult hiervoor in principe vooraf een kostenbegroting ontvangen. Deze kosten moet u zelf betalen.</p></div></div>
    <div class="vcard"><div class="img" role="img" aria-label="Overleg met documenten aan tafel"></div><div><h3>Gemachtigde zorg</h3><p>Bij bepaalde behandelingen is er toestemming nodig van de zorgverzekeraar. Er zal dan een machtiging aangevraagd moeten worden bij de zorgverzekeraar, zodat de kosten (deels) vergoed worden.</p></div></div>
    <div class="vcard"><div class="img" role="img" aria-label="Handen op een rekenmachine met munten"></div><div><h3>Tarieven</h3><p>De tarieven voor de mondzorg zijn vastgesteld volgens de landelijke zorgautoriteit. Een overzicht van de tarieven vindt u hier.</p></div></div>
  </div>
  <footer class="site-footer">
    <svg class="wave" viewBox="0 0 475 42" preserveAspectRatio="none"><path d="M0 42 L0 14 C130 44 300 40 475 0 L475 42Z" fill="#2b9ad8"/><path d="M0 42 L0 24 C130 50 310 42 475 14 L475 42Z" fill="#323d52"/></svg>
    <div class="footer-body">
      <div class="footer-brand">Vro Klinieken</div>
      <div class="footer-col links"><h4>Quick links</h4><ul><li>Home</li><li>Over ons</li><li>Vergoeding</li><li>Klachtbehandeling</li><li>Duurzaamheid</li><li>Duurzame mondzorg</li><li>Contact</li></ul></div>
      <div class="footer-col details"><h4>Contact details</h4>
        <div class="detail"><i class="ic"></i><span>Lindenhof 14<br>2711 AB Zoetermeer</span></div>
        <div class="detail"><i class="ic"></i><span>Phone Number<br>079 204 5518</span></div>
        <div class="detail"><i class="ic"></i><span>Mail ID:<br>info@vroklinieken.nl</span></div>
      </div>
      <div class="footer-rule"></div>
      <div class="copy">Copyrights @ 2023 Vro Klinieken. All Rights Reserved.</div>
    </div>
  </footer>
</section>

<section class="page" style="left:490px;top:988px;height:772px">
  <header class="site-header">
    <div class="brand">Vro Klinieken</div>
    <div class="contact-chip"><span class="chip-dot"></span><span>Mail:<br>info@vroklinieken.nl</span></div>
    <div class="contact-chip"><span class="chip-dot"></span><span>Phone Number<br>079 204 5518</span></div>
    <div class="btn">Make an appointment</div>
  </header>
  <nav class="site-nav"><a>Home</a><a>Over ons</a><a>Vergoeding</a><a>Klachtbehandeling</a><a class="active">Duurzaamheid / Duurzame mondzorg</a><a>Contact</a></nav>
  <div class="hero">
    <div class="photo" role="img" aria-label="Patiënte in de behandelstoel met tandarts"></div>
    <h1 class="small" style="top:28px">Duurzaamheid/<br>duurzame<br>mondzorg</h1>
    <svg class="wave" viewBox="0 0 475 40" preserveAspectRatio="none"><path d="M0 40 L0 20 C140 -4 330 12 475 4 L475 40Z" fill="#2b9ad8"/><path d="M0 40 L0 28 C150 6 330 26 475 14 L475 40Z" fill="#6b7fa0"/><path d="M0 40 L0 34 C150 14 330 32 475 20 L475 40Z" fill="#fff"/></svg>
  </div>
  <h2 class="section-title">Duurzaamheid/duurzame mondzorg</h2>
  <div class="framed" role="img" aria-label="Lachende vrouw aan de telefoon achter een bureau" style="background:linear-gradient(120deg,#e7e4df 0%,#c9d4de 50%,#a9bccd 100%)"></div>
  <p class="body-text" style="margin-top:18px">Klimaatverandering en duurzaamheid spelen een steeds grotere rol in ons dagelijks leven. Volgens landelijk onderzoek is de zorg verantwoordelijk voor zo'n 7 procent van de nationale klimaatvoetafdruk. Vro Klinieken houdt zich daarom ook bezig met verduurzaming. Samen met de beroepsvereniging (GVLS) hebben wij gekeken naar verduurzaming van de praktijk en inrichting, zonder daarbij in te leveren op de kwaliteit en hygiëne. Voorbeelden hiervan zijn digitale verwijzingen, folders digitaal versturen en het reduceren van verbruiksmaterialen.</p>
  <footer class="site-footer">
    <svg class="wave" viewBox="0 0 475 42" preserveAspectRatio="none"><path d="M0 42 L0 14 C130 44 300 40 475 0 L475 42Z" fill="#2b9ad8"/><path d="M0 42 L0 24 C130 50 310 42 475 14 L475 42Z" fill="#323d52"/></svg>
    <div class="footer-body">
      <div class="footer-brand">Vro Klinieken</div>
      <div class="footer-col links"><h4>Quick links</h4><ul><li>Home</li><li>Over ons</li><li>Vergoeding</li><li>Klachtbehandeling</li><li>Duurzaamheid</li><li>Duurzame mondzorg</li><li>Contact</li></ul></div>
      <div class="footer-col details"><h4>Contact details</h4>
        <div class="detail"><i class="ic"></i><span>Lindenhof 14<br>2711 AB Zoetermeer</span></div>
        <div class="detail"><i class="ic"></i><span>Phone Number<br>079 204 5518</span></div>
        <div class="detail"><i class="ic"></i><span>Mail ID:<br>info@vroklinieken.nl</span></div>
      </div>
      <div class="footer-rule"></div>
      <div class="copy">Copyrights @ 2023 Vro Klinieken. All Rights Reserved.</div>
    </div>
  </footer>
</section>

<section class="page" style="left:970px;top:988px;height:867px">
  <header class="site-header">
    <div class="brand">Vro Klinieken</div>
    <div class="contact-chip"><span class="chip-dot"></span><span>Mail:<br>info@vroklinieken.nl</span></div>
    <div class="contact-chip"><span class="chip-dot"></span><span>Phone Number<br>079 204 5518</span></div>
    <div class="btn">Make an appointment</div>
  </header>
  <nav class="site-nav"><a>Home</a><a>Over ons</a><a>Vergoeding</a><a class="active">Klachtbehandeling</a><a>Duurzaamheid / Duurzame mondzorg</a><a>Contact</a></nav>
  <div class="hero">
    <div class="photo" role="img" aria-label="Patiënte in de behandelstoel met tandarts"></div>
    <h1 class="small" style="top:40px">Klachtbehandeling</h1>
    <svg class="wave" viewBox="0 0 475 40" preserveAspectRatio="none"><path d="M0 40 L0 20 C140 -4 330 12 475 4 L475 40Z" fill="#2b9ad8"/><path d="M0 40 L0 28 C150 6 330 26 475 14 L475 40Z" fill="#6b7fa0"/><path d="M0 40 L0 34 C150 14 330 32 475 20 L475 40Z" fill="#fff"/></svg>
  </div>
  <h2 class="section-title">Klachtenprocedure bij Vro Klinieken</h2>
  <p class="body-text" style="margin-top:12px;padding:0 70px;font-size:4.8px">Wij streven uiteraard naar de hoogste kwaliteit van zorg en patiënttevredenheid. Mocht u onverhoopt niet tevreden zijn over onze dienstverlening, dan horen wij dat graag zodat we het kunnen oplossen. Dit kan uiteraard door opnieuw een afspraak te maken of een eventuele mail/brief te schrijven naar info@vroklinieken.nl.</p>
  <div class="kgrid">
    <div class="kcard"><div class="img" role="img" aria-label="Arts in gesprek met een patiënte"></div><h3>DIRECTE COMMUNICATIE</h3><p>Wij moedigen u aan om eventuele zorgen of ontevredenheid eerst te bespreken met de betrokken zorgverlener of medewerker. Vaak kan een open dialoog leiden tot een oplossing voor beide partijen.</p></div>
    <div class="kcard"><div class="img" role="img" aria-label="Arts in overleg met een patiënte"></div><h3>BEHANDELING VAN DE KLACHT</h3><p>Wij zullen uw klacht serieus nemen en zo snel mogelijk behandelen. Ons team zal er alles aan doen om een passende oplossing te vinden en herhaling te voorkomen.</p></div>
    <div class="kcard"><div class="img" role="img" aria-label="Tandarts behandelt een patiënte"></div><h3>VERBETERING VAN ONZE ZORG</h3><p>Uw feedback, positief of kritisch, is voor ons waardevol. Het stelt ons in staat om onze dienstverlening voortdurend te verbeteren en de best mogelijke zorg te bieden aan al onze patiënten.</p></div>
    <div class="kcard"><div class="img" role="img" aria-label="Jong meisje bij de tandarts"></div><h3>EXTERNE GESCHILLENINSTANTIE</h3><p>Indien de klacht niet naar tevredenheid is opgelost, kunt u zich wenden tot de onafhankelijke klachtenregeling via de GVLS. Wij hechten waarde aan uw input en streven ernaar om uw klacht zorgvuldig af te handelen.</p></div>
  </div>
  <footer class="site-footer">
    <svg class="wave" viewBox="0 0 475 42" preserveAspectRatio="none"><path d="M0 42 L0 14 C130 44 300 40 475 0 L475 42Z" fill="#2b9ad8"/><path d="M0 42 L0 24 C130 50 310 42 475 14 L475 42Z" fill="#323d52"/></svg>
    <div class="footer-body">
      <div class="footer-brand">Vro Klinieken</div>
      <div class="footer-col links"><h4>Quick links</h4><ul><li>Home</li><li>Over ons</li><li>Vergoeding</li><li>Klachtbehandeling</li><li>Duurzaamheid</li><li>Duurzame mondzorg</li><li>Contact</li></ul></div>
      <div class="footer-col details"><h4>Contact details</h4>
        <div class="detail"><i class="ic"></i><span>Lindenhof 14<br>2711 AB Zoetermeer</span></div>
        <div class="detail"><i class="ic"></i><span>Phone Number<br>079 204 5518</span></div>
        <div class="detail"><i class="ic"></i><span>Mail ID:<br>info@vroklinieken.nl</span></div>
      </div>
      <div class="footer-rule"></div>
      <div class="copy">Copyrights @ 2023 Vro Klinieken. All Rights Reserved.</div>
    </div>
  </footer>
</section>

</div>
</body>
</html>
```